Vantor Reach needs a Business Card Design

We need a business card design for an Information Technology company based in Fairfax Virginia called Vantor Reach. We want the business card to use our logo colors. We need it to be double-sided. The business card needs to look professional but we would like it to be unique. You can get company information from our web site (http://www.vantorreachllc.example).

Target Market(s)

Target market is Government Agencies and Business Professionals.

Industry/Entity Type

Business

Requirements
Must have
• Must have section for company name, company address, company URL, employee name, title, phone and email. Also must have company logo and space for entering logos.

```html
<!DOCTYPE html>
<html lang="en">
<head>
<meta charset="utf-8">
<title>Vantor Reach – Business Card</title>
<link href="https://fonts.googleapis.com/css2?family=Open+Sans:wght@400;600;700&display=swap" rel="stylesheet">
<style>
  :root {
    --page-bg: #e6e8ec;
    --sky-blue: #1d8bd6;
    --royal-blue: #3a4fb0;
    --ink-blue: #2c3f9e;
    --card-white: #ffffff;
    --faint-grey: #eef0f3;
    --shadow: rgba(20, 30, 60, 0.18);
  }
  * { box-sizing: border-box; margin: 0; padding: 0; }
  html, body {
    width: 1200px; height: 900px; overflow: hidden;
    background: var(--page-bg);
    font-family: "Open Sans", Arial, sans-serif;
  }
  .sheet {
    width: 1200px; height: 900px;
    display: flex; flex-direction: column; align-items: center; justify-content: center;
    gap: 44px;
  }
  .card {
    position: relative; width: 630px; height: 360px; overflow: hidden;
    box-shadow: 0 10px 28px var(--shadow);
  }

  /* Back side */
  .card-back { background: var(--sky-blue); }
  .card-back .brand {
    position: absolute; left: 0; right: 0; top: 128px;
    display: flex; flex-direction: column; align-items: center; gap: 6px;
    color: var(--card-white);
  }
  .brand-row { display: flex; align-items: center; gap: 14px; }
  .brand-square { width: 34px; height: 34px; background: var(--card-white); }
  .brand-name { font-size: 36px; font-weight: 700; letter-spacing: 1px; text-transform: uppercase; }
  .brand-tagline { font-size: 10px; font-weight: 600; letter-spacing: 1.2px; text-transform: uppercase; opacity: 0.85; padding-left: 48px; }
  .web-band {
    position: absolute; right: 0; bottom: 0; width: 345px; height: 50px;
    background: var(--royal-blue); color: var(--card-white);
    display: flex; align-items: center; gap: 22px; padding-left: 22px;
    font-size: 15px;
  }
  .web-band svg { width: 22px; height: 16px; }

  /* Front side */
  .card-front { background: var(--card-white); }
  .faint-mark { position: absolute; left: 80px; top: -30px; width: 170px; height: 170px; background: var(--faint-grey); }
  .front-brand { position: absolute; left: 36px; top: 58px; color: var(--royal-blue); }
  .front-brand .brand-row { gap: 10px; }
  .front-brand .brand-square { width: 22px; height: 22px; background: var(--royal-blue); }
  .front-brand .brand-name { font-size: 24px; }
  .front-brand .brand-tagline { font-size: 7px; padding-left: 32px; color: var(--royal-blue); }

  .person-band {
    position: absolute; right: 0; top: 84px; width: 272px; height: 66px;
    background: var(--royal-blue); color: var(--card-white);
    padding: 10px 0 0 28px;
  }
  .person-name { font-size: 19px; font-weight: 700; line-height: 1.2; }
  .person-title { font-size: 15px; line-height: 1.2; }

  .contact-rule { position: absolute; left: 316px; top: 122px; width: 4px; height: 130px; background: var(--royal-blue); }
  .contact-list {
    position: absolute; left: 338px; top: 162px; list-style: none;
    color: var(--ink-blue); font-size: 12.5px; line-height: 1.35;
  }
  .contact-list li { display: flex; align-items: flex-start; gap: 8px; margin-bottom: 6px; }
  .contact-list svg { width: 13px; height: 13px; flex: none; margin-top: 2px; }
  .contact-list b { font-weight: 700; }
  .icon-gap { width: 13px; flex: none; }

  .accent-band { position: absolute; left: 0; bottom: 0; width: 390px; height: 22px; background: var(--sky-blue); }
</style>
</head>
<body>
<main class="sheet">

  <section class="card card-back" aria-label="Business card back">
    <div class="brand">
      <div class="brand-row">
        <span class="brand-square"></span>
        <span class="brand-name">Vantor Reach</span>
      </div>
      <span class="brand-tagline">Turning Ideas Into Working Systems</span>
    </div>
    <div class="web-band">
      <svg viewBox="0 0 22 16" aria-hidden="true"><path d="M0 6h13V1l9 7-9 7V10H0z" fill="#fff"/></svg>
      <span>www.vantorreachllc.example</span>
    </div>
  </section>

  <section class="card card-front" aria-label="Business card front">
    <div class="faint-mark"></div>
    <div class="front-brand">
      <div class="brand-row">
        <span class="brand-square"></span>
        <span class="brand-name">Vantor Reach</span>
      </div>
      <span class="brand-tagline">Turning Ideas Into Working Systems</span>
    </div>

    <div class="person-band">
      <div class="person-name">Daniel Reyes</div>
      <div class="person-title">President</div>
    </div>

    <div class="contact-rule"></div>
    <ul class="contact-list">
      <li>
        <svg viewBox="0 0 14 14" aria-hidden="true"><path d="M7 0a5 5 0 0 0-5 5c0 4 5 9 5 9s5-5 5-9a5 5 0 0 0-5-5zm0 7a2 2 0 1 1 0-4 2 2 0 0 1 0 4z" fill="#2c3f9e"/></svg>
        <span>Meridian Ave, Suite 310 4820<br>Larkfield, VA 22099</span>
      </li>
      <li>
        <span class="icon-gap"></span>
        <span><b>P :</b> 877.555.0142<br><b>F :</b> 888.555.0187</span>
      </li>
      <li>
        <svg viewBox="0 0 14 14" aria-hidden="true"><rect x="0.5" y="2.5" width="13" height="9" fill="#2c3f9e"/><path d="M1 3l6 5 6-5" stroke="#fff" fill="none"/></svg>
        <span>info@vantorreachllc.example</span>
      </li>
      <li>
        <svg viewBox="0 0 14 14" aria-hidden="true"><circle cx="7" cy="7" r="6" fill="none" stroke="#2c3f9e" stroke-width="1.3"/><path d="M1 7h12M7 1c-3 3-3 9 0 12M7 1c3 3 3 9 0 12" fill="none" stroke="#2c3f9e"/></svg>
        <span>www.vantorreachllc.example</span>
      </li>
    </ul>

    <div class="accent-band"></div>
  </section>

</main>
</body>
</html>
```